" Fornecemos infra estrutura para empresas, possuímos uma rede de fibra óptica própria cobrindo diversas cidades, provendo conexão a internet, telefonia voip, transporte de dados, temos um datacenter, fornecemos soluções de cloud computing, cloud pabx. "

```html
<!DOCTYPE html>
<html lang="pt-BR">
<head>
<meta charset="utf-8">
<title>Assinatura de e-mail – Vireon Telecom</title>
<link href="https://fonts.googleapis.com/css2?family=Roboto:wght@400;700&display=swap" rel="stylesheet">
<style>
  :root {
    --page-bg: #e9ebee;
    --card-bg: #ffffff;
    --text-dark: #2b2b2b;
    --text-muted: #555555;
    --brand-blue: #1e9fd6;
    --brand-navy: #161d45;
    --brand-mid: #2a6fb0;
  }
  * { margin: 0; padding: 0; box-sizing: border-box; }
  html, body {
    width: 1200px; height: 1200px; overflow: hidden;
    background: var(--page-bg);
    font-family: "Roboto", Arial, sans-serif;
  }
  .signature {
    position: absolute; left: 100px; top: 490px;
    width: 1000px; height: 220px;
    background: var(--card-bg);
    box-shadow: 0 2px 8px rgba(0,0,0,0.12);
  }
  .identity {
    position: absolute; left: 100px; top: 40px; width: 300px;
    text-align: center;
  }
  .brand {
    display: flex; align-items: center; justify-content: center; gap: 14px;
    height: 60px;
  }
  .brand-dot {
    width: 52px; height: 52px; border-radius: 50%;
    background: var(--brand-mid);
  }
  .brand-name {
    font-size: 34px; font-weight: 700; color: var(--brand-navy);
    letter-spacing: 1px;
  }
  .person-name {
    margin-top: 24px;
    font-size: 19px; font-weight: 700; color: var(--text-dark);
  }
  .person-role {
    margin-top: 8px;
    font-size: 11px; color: var(--text-muted); letter-spacing: 0.5px;
  }
  .contacts {
    position: absolute; left: 440px; top: 14px;
    list-style: none;
  }
  .contact {
    display: flex; align-items: flex-start; gap: 14px;
    font-size: 18px; color: var(--text-dark);
    line-height: 22px; margin-bottom: 17px;
  }
  .contact svg { width: 20px; height: 20px; flex: none; margin-top: 1px; fill: var(--text-dark); }
  .contact-address { font-size: 16px; line-height: 19px; }
  .bands {
    position: absolute; left: 0; bottom: 8px; width: 1000px; height: 26px;
  }
</style>
</head>
<body>
  <section class="signature">
    <div class="identity">
      <div class="brand">
        <span class="brand-dot"></span>
        <span class="brand-name">Vireon Telecom</span>
      </div>
      <p class="person-name">Nome Sobrenome</p>
      <p class="person-role">FUNÇÃO</p>
    </div>

    <ul class="contacts">
      <li class="contact">
        <svg viewBox="0 0 20 20"><path d="M2 4h16v12H2z M3 5l7 6 7-6" fill="none" stroke="#2b2b2b" stroke-width="0"/><path d="M2 4h16v12H2zM3.5 5.5v9h13v-9L10 11z"/></svg>
        <span>contato@empresa.com.br</span>
      </li>
      <li class="contact">
        <svg viewBox="0 0 20 20"><path d="M5 2l3 0 1 4-2 1.5c1 2.2 2.8 4 5 5L13.5 11l4 1v3c0 1-1 2-2 2C8.5 17 3 11.5 3 4.5 3 3 4 2 5 2z"/></svg>
        <span>(xx) x xxxx-xxxx</span>
      </li>
      <li class="contact">
        <svg viewBox="0 0 20 20"><path d="M6 1h8a1.5 1.5 0 0 1 1.5 1.5v15A1.5 1.5 0 0 1 14 19H6a1.5 1.5 0 0 1-1.5-1.5v-15A1.5 1.5 0 0 1 6 1zM6.5 3v12h7V3zM10 15.8a1 1 0 1 0 0 2 1 1 0 0 0 0-2z"/></svg>
        <span>(xx) x xxxx-xxxx</span>
      </li>
      <li class="contact contact-address">
        <svg viewBox="0 0 20 20"><path d="M10 1a6 6 0 0 1 6 6c0 4.5-6 12-6 12S4 11.5 4 7a6 6 0 0 1 6-6zm0 3.5a2.5 2.5 0 1 0 0 5 2.5 2.5 0 0 0 0-5z"/></svg>
        <span>Rua desconhecida, xxxx<br>desconhecido</span>
      </li>
    </ul>

    <svg class="bands" viewBox="0 0 1000 26" aria-hidden="true">
      <rect x="0" y="10" width="1000" height="9" fill="var(--brand-blue)"/>
      <polygon points="560,2 1000,2 1000,26 536,26" fill="var(--brand-navy)"/>
    </svg>
  </section>
</body>
</html>
```